CD-/Plattencover für Band
Zielgruppe
Bandname:
Glutwerk
Album Titel:
Nebelgrauer Pfad
Musikvideo:
https://www.clipwelle.example/watch?v=Q7T3kaPmXRe
Unsere Musik ist im wahrsten Sinn des Wortes Glutiger Pfad. Schwere Texte die nicht immer gut schmecken aber immer mit Lösungsansatz die in vielen Lebenslagen helfen und unterstützen sollen.
Nebelgraue Erzählungen“ wie man sie aus dem herausfordernden Leben kennt, verpackt in Stoffig Rockigen Sound.
Zielgruppe:
Musikinteressiert ab 25 Jahren / alleinstehende Mütter / Personen in Sinnkrisen / Personen die jemanden verloren haben / Personen mit psychischen Problemen / Personen die an einem Wendepunkt kommen / Personen die sich privat oder Beruflich verändern möchten
Positionierung:
Zusammenführung von modernem Heavy Rock und Mundart Texten, irgendwo zwischen Konrad von Wettlach und Zwirnbögl
Songinhalte:
Mobbing / Nostalgie / Beziehungen / Veränderungen / Trauer / Depression / Angststörung / Mut / Zusammenhalt / Liebe / Enttäuschungen / Selbstfindung / Musikindustrie
Aufgabenstellung
Das Bandfoto dient nur zur Info. Das Logo soll aufs Cover.
Design: Cool, Modern, Rockig, Bodenständig angelehnt und passend zum Logo.
Im Mittelpunkt soll ein Lollipop stehen der dann auch als Markenzeichen dienen soll. Mit dem Lollipop soll der Albumtitel(Nebelgrauer Pfad) dargestellt werden. Der Lolli steht für Süß. Für Bitter könnte der Lolli die Form eines Blattes haben oder er könnte eine außergewöhnliche Farbe haben oder es könnten sich Dornen und Blätter am Lollpop Stiel entlag schlingen. Die zentrale Farbe/Hintergrund soll Magenta sein.

```html
<!DOCTYPE html>
<html lang="de">
<head>
<meta charset="utf-8">
<title>Glutwerk – Nebelgrauer Pfad</title>
<link rel="stylesheet" href="https://fonts.googleapis.com/css2?family=Playfair+Display:wght@900&family=Great+Vibes&display=swap">
<style>
  :root {
    --magenta: #d42a86;
    --magenta-light: #f27ab9;
    --magenta-glow: #ffb3dc;
    --ink: #0d0a0c;
    --chalk: #fbf5f1;
  }
  html, body {
    margin: 0;
    padding: 0;
    width: 1200px;
    height: 1200px;
    overflow: hidden;
    background: var(--magenta);
  }
  .cover {
    position: relative;
    width: 1200px;
    height: 1200px;
    background: var(--magenta);
    overflow: hidden;
  }
  .band-name {
    position: absolute;
    top: 22px;
    left: 0;
    width: 100%;
    text-align: center;
    font-family: "Playfair Display", Georgia, serif;
    font-weight: 900;
    font-size: 52px;
    line-height: 1;
    color: var(--ink);
    margin: 0;
  }
  .lollipop-art {
    position: absolute;
    left: 0;
    top: 0;
    width: 1200px;
    height: 1200px;
  }
  .album-title {
    position: absolute;
    left: 0;
    top: 0;
    width: 1200px;
    height: 1200px;
    margin: 0;
    font-weight: normal;
  }
  .title-block {
    position: absolute;
    left: 0;
    width: 100%;
    text-align: center;
    top: 400px;
    font-family: "Playfair Display", Georgia, serif;
    font-weight: 900;
    font-size: 380px;
    line-height: 1;
    letter-spacing: 0.04em;
    color: var(--ink);
  }
  .title-script {
    position: absolute;
    left: 0;
    width: 100%;
    text-align: center;
    top: 470px;
    font-family: "Great Vibes", cursive;
    font-size: 200px;
    line-height: 1;
    color: var(--chalk);
    transform: rotate(-4deg);
    text-shadow: 0 0 10px rgba(255,255,255,0.8), 0 0 26px rgba(255,255,255,0.45);
  }
</style>
</head>
<body>
<main class="cover">
  <p class="band-name">Glutwerk</p>

  <svg class="lollipop-art" role="img" aria-label="Illustration: pinker Lollipop mit Dornen am Rand vor einem strahlenden Lichtkranz, Stiel nach unten" viewBox="0 0 1200 1200">
    <defs>
      <radialGradient id="burst-glow" cx="600" cy="560" r="470" gradientUnits="userSpaceOnUse">
        <stop offset="0" stop-color="var(--magenta-glow)"/>
        <stop offset="0.45" stop-color="var(--magenta-light)"/>
        <stop offset="1" stop-color="var(--magenta)" stop-opacity="0"/>
      </radialGradient>
    </defs>
    <rect x="0" y="0" width="1200" height="1200" fill="url(#burst-glow)"/>
  </svg>

  <h1 class="album-title">
    <span class="title-block">PFAD</span>
    <span class="title-script">nebelgrauer</span>
  </h1>
</main>
</body>
</html>
```